Flyer-Design, Thema Kindergeburtstag
Zielgruppe
Wir sind eine Foto-Studio, in dem man auch Kindergeburtstage feiern kann. Infos dazu auf https://plinvofoto.de/kinder-foto-party-kindergeburtstag-witten/
Für die Zielgruppe der Eltern (und deren Kinder) benötigen wir einen Flyer, der unser Angebot umfassend darstellt.
Aufgabenstellung
Unser Angebot 'Kindergeburtstag feiern in Witten' soll bitte visuell für einen Flyer umgesetzt werden.
Da wir recht viel Content (Text und Bild) hierfür bereits besitzen, ist auch ein größerer Flyer (Leporello z.B.) gerne möglich.
Es können alle Bilder und Texte von https://plinvofoto.de/kinder-foto-party-kindergeburtstag-witten/ verwendet werden für den Flyer. Auch unser Logo von PlinvoFoto.de
Bauen Sie den Inhalt bitte logisch auf:
1. Was bieten wir (Kindergeburtstage mit vielen verschiedenen Aktionen und Animationen)
2. Wo bieten wir es an (Witten, bei Dortmund)
3. Welche Aktionen und Animationen bieten wir genau an (Auflistung mit einigen passenden Bildern)
4. Buchung und Preise
Folgende Highlights/Themen sollen eine eigene Überschrift oder Spalte bekommen:
- Fotograf und Bilder
- Kostüm-Verleih
- PhotoBooth-System
- Kinder-Schminken
- Hüpfburg
- Sumo-Anzüge und Gladiator-Games
- Image-Video (https://www.videoportal-beispiel.de/watch?v=Qmtarb7Lx0e&feature=emb_title/, siehe https://plinvofoto.de/kinder-foto-party-kindergeburtstag-witten/ oben, Link auch als QR-Code einbinden)
Der Flyer soll schön bunt und phantasievoll werden.
Die Bilder erhalten Sie in hoher Auflösung, wenn nach Vergabe benötigt. Für den ersten Entwurf bitte die Bilder auf https://plinvofoto.de/kinder-foto-party-kindergeburtstag-witten/ einfach downloaden.
Logo-Download:
https://dateiablage-beispiel.de/open?id=4Gt7wRmc2Lpz9XbQe0Hn5VkDsYa1UoJfT
https://dateiablage-beispiel.de/open?id=8q_KwTNZE41pRsXmC_7HvLd2Ybe_Ju-QW

```html
<!DOCTYPE html>
<html lang="de">
<head>
<meta charset="utf-8">
<title>Kindergeburtstag Witten – Flyer Titelseite</title>
<link rel="stylesheet" href="https://fonts.googleapis.com/css2?family=Bebas+Neue&family=Montserrat:wght@400&display=swap">
<style>
  :root {
    --magenta-deep: #8e1344;
    --magenta: #d0246a;
    --pink-glow: #e95a91;
    --haze: #d9d6dc;
    --teal: #5cc4b5;
    --green: #7fa88a;
    --violet: #6a4f9a;
    --white: #ffffff;
  }
  * { margin: 0; padding: 0; box-sizing: border-box; }
  html, body {
    width: 1200px;
    height: 900px;
    overflow: hidden;
    background: #cfd0d2;
  }
  .cover {
    position: relative;
    width: 1200px;
    height: 900px;
    overflow: hidden;
  }
  .cover-photo {
    position: absolute;
    inset: 0;
    background:
      radial-gradient(ellipse 45% 40% at 88% 12%, var(--teal) 0%, transparent 70%),
      radial-gradient(ellipse 40% 45% at 85% 75%, var(--green) 0%, transparent 70%),
      radial-gradient(ellipse 25% 25% at 58% 85%, var(--violet) 0%, transparent 75%),
      radial-gradient(ellipse 35% 45% at 62% 35%, var(--haze) 0%, transparent 75%),
      linear-gradient(100deg, var(--magenta-deep) 0%, var(--magenta) 25%, var(--pink-glow) 45%, #c9a8b8 62%, #a9c9c2 80%, var(--teal) 100%);
  }
  .cover-title {
    position: absolute;
    left: 80px;
    top: 70px;
    font-family: "Bebas Neue", "Oswald", sans-serif;
    font-size: 205px;
    line-height: 0.84;
    font-weight: 400;
    color: var(--white);
    letter-spacing: 2px;
    text-transform: uppercase;
    opacity: 0.95;
  }
  .cover-title span { display: block; }
  .brand {
    position: absolute;
    left: 400px;
    top: 704px;
    display: flex;
    align-items: center;
    gap: 18px;
    color: var(--white);
    font-family: "Montserrat", sans-serif;
  }
  .brand-mark {
    width: 58px;
    height: 58px;
    border: 3px solid var(--white);
    border-radius: 50%;
  }
  .brand-name {
    font-size: 44px;
    font-weight: 400;
    line-height: 1;
  }
</style>
</head>
<body>
  <main class="cover">
    <div class="cover-photo" role="img" aria-label="Foto: verkleidete Kinder feiern im Konfettiregen, links pinkes Konfetti, rechts türkises Licht"></div>
    <h1 class="cover-title">
      <span>Kinder</span>
      <span>Geburtstag</span>
      <span>Witten</span>
    </h1>
    <div class="brand">
      <div class="brand-mark"></div>
      <div class="brand-name">PlinvoFoto.de</div>
    </div>
  </main>
</body>
</html>
```